website re-design for: fern+lantern, complete vision care

we are a growing, cutting edge eye clinic with two locations in the palouse area of washington state, in the usa. we offer complete vision care, from spectacles and contacts to ocular disease management and treatment.

our current website was designed as a freebie, and was always meant to be a placeholder. we have reached a point where we would like our website to have a more stand-apart look and feel, while maintaining an intuitive user experience.

Target Market(s)

because our two clinics serve vastly different demographics, the website will have to speak to both. one clinic is located in a college town (majority of patients are 18-50 years+), while the other serves an older adult population (majority of patients 30-75 yrs+).

Industry/Entity Type

Health And Wellness

Logo Text

fern+lantern (including a logo lock-up version w/ "complete vision care")

Coding

Coded - Design and coding required

Number of Pages Required

5+ page

Font styles to use
Sans Serif
Other font styles liked:
• Verdana, and complementary fonts

Colors
606060
ffffff
33b8a4
86cfc6

Requirements
Must have
• - Pertinent contact information w/ Google maps
• - Clinic phone numbers at top of each page
• - An appointment request form
• - Page for Blog
• - Integrate with overall brand look and feel (e.g. Verdana font (we are open to complementary fonts), all lower case, except for prose,
• - Mobile friendly design
• - Code to maximize Search Engine Optimization (SEO)
Nice to have
• a design that speaks to the true nature of our business as an eye clinic, but feels different than typical eye care websites
Should not have
• this probably goes without saying, but the website should not have any political slant or otherwise bias

```html
<!DOCTYPE html>
<html lang="en">
<head>
<meta charset="utf-8">
<title>fern+lantern — complete vision care</title>
<link href="https://fonts.googleapis.com/css2?family=Montserrat:wght@400;500;600;700&family=Open+Sans:wght@400;600&display=swap" rel="stylesheet">
<style>
:root{
  --accent:#33b8a4;
  --accent-soft:#86cfc6;
  --ink:#2e2e2e;
  --text:#606060;
  --muted:#9a9a9a;
  --soft:#f4f8f7;
  --line:#e2e8e7;
  --white:#ffffff;
  --dark1:#1f2726;
  --dark2:#273130;
  --dark3:#2f3a39;
}
*{box-sizing:border-box;margin:0;padding:0}
html,body{width:1200px;height:5357px;overflow:hidden}
body{position:relative;background:var(--white);font-family:"Open Sans",Verdana,sans-serif;color:var(--text);font-size:11px;line-height:1.6}
h1,h2,h3,h4,.btn,.nav a,.brand,.partner,.link,.cat,.meta b,.per{font-family:"Montserrat",Verdana,sans-serif;text-transform:lowercase}
section,header,footer{position:absolute;left:0;width:1200px}
.abs{position:absolute}
.btn{display:inline-block;font-size:9px;font-weight:600;letter-spacing:.06em;padding:9px 18px;text-align:center;white-space:nowrap}
.btn-white{background:var(--white);color:var(--ink)}
.btn-accent{background:var(--accent);color:var(--white)}
.btn-outline-white{border:1px solid var(--white);color:var(--white)}
.btn-outline-accent{border:1px solid var(--accent);color:var(--accent)}
.bar{width:34px;height:3px;background:var(--accent)}
.photo{position:absolute}

/* nav */
.nav{top:0;height:36px;background:var(--white);z-index:2;display:flex;justify-content:center;align-items:center;gap:26px}
.nav a{font-size:10px;font-weight:600;color:var(--ink);text-decoration:none}
.nav .brand{position:absolute;left:30px;top:10px;font-size:12px;font-weight:700;color:var(--accent)}
.nav .phones{position:absolute;right:30px;top:11px;font-size:9px;color:var(--text);display:flex;gap:14px;align-items:center}
.nav .phones svg{vertical-align:-2px;margin-right:4px}

/* hero */
.hero{top:36px;height:321px}
.hero .photo{inset:0;background:linear-gradient(100deg,#9fb3b0 0%,#7f9592 30%,#afc2bf 60%,#cfdcda 100%)}
.hero h1{left:0;width:1200px;padding-left:100px;text-align:center;top:88px;font-size:33px;font-weight:700;color:var(--white)}
.hero p{left:515px;top:142px;width:330px;text-align:center;color:var(--white);font-size:10px;line-height:1.5}
.hero .b1{left:475px;top:212px;width:112px}
.hero .b2{left:625px;top:212px;width:125px}

/* what we do */
.what{top:375px;height:330px}
.what h2{left:240px;top:20px;font-size:24px;font-weight:700;line-height:1.1;color:var(--ink)}
.what .bar{left:240px;top:86px}
.what .intro{left:428px;top:20px;width:530px}
.feature{position:absolute;width:200px}
.feature svg{position:absolute;left:0;top:0}
.feature h4{margin-left:28px;font-size:11px;font-weight:600;color:var(--ink)}
.feature p{margin-left:28px;font-size:9px;line-height:1.5}

/* unique band */
.unique{top:725px;height:115px;background:var(--accent-soft)}
.unique h2{left:243px;top:24px;font-size:19px;font-weight:700;color:var(--white)}
.unique .bar{left:243px;top:52px;background:var(--white)}
.unique p{left:243px;top:62px;width:520px;color:var(--white);font-size:9px}
.unique .btn{left:820px;top:42px;width:137px}

/* pricing */
.pricing{top:857px;height:470px}
.pricing h2{left:0;width:1200px;top:22px;text-align:center;font-size:15px;font-weight:700;color:var(--ink)}
.pricing .bar{left:583px;top:48px}
.plan{position:absolute;top:72px;height:392px;background:var(--soft);text-align:center}
.plan svg{margin-top:38px}
.plan h4{font-size:11px;font-weight:600;color:var(--ink);margin-top:8px}
.plan .price{font-family:"Montserrat",sans-serif;font-size:30px;font-weight:700;color:var(--ink);line-height:1.1;margin-top:6px}
.plan .per{font-size:8px;color:var(--muted)}
.plan ul{list-style:none;margin:22px 0 26px;font-size:9px;color:var(--muted);line-height:2.2}

/* about band */
.about{top:1346px;height:279px;background:var(--accent-soft);text-align:center}
.about h2{left:0;width:1200px;top:70px;font-size:20px;font-weight:700;color:var(--white)}
.about .bar{left:583px;top:102px;background:var(--white)}
.about p{left:240px;width:720px;top:112px;color:var(--white);font-size:9px}
.about .btn{left:540px;top:170px;width:120px}

/* services icons */
.services{top:1660px;height:380px}
.svc{position:absolute;width:230px;text-align:center}
.svc .circ{width:44px;height:44px;border-radius:50%;background:var(--soft);margin:0 auto 14px;display:flex;align-items:center;justify-content:center}
.svc h4{font-size:11px;font-weight:600;color:var(--ink)}
.svc p{font-size:9px;line-height:1.5}

/* split */
.split{height:447px}
.split .textside{position:absolute;top:0;width:600px;height:447px;background:var(--soft);text-align:center}
.split h3{margin-top:175px;font-size:14px;font-weight:700;color:var(--ink)}
.split p{width:340px;margin:14px auto 0;font-size:9px;color:var(--muted)}
.split .link{display:inline-block;margin-top:18px;font-size:9px;color:var(--accent);border-bottom:1px solid var(--accent);letter-spacing:.04em}

/* testimonial */
.testi{top:2964px;height:150px}
.testi .avatar{left:314px;top:28px;width:104px;height:104px;border-radius:50%;background:linear-gradient(135deg,#d8dcd9,#8f9c99)}
.testi h4{left:432px;top:32px;font-size:12px;font-weight:700;color:var(--ink)}
.testi .role{left:432px;top:50px;font-size:8px;color:var(--muted)}
.testi p{left:432px;top:66px;width:480px;font-size:10px;line-height:1.5}
.testi .arrow{top:72px;font-size:14px;color:var(--muted)}

/* team */
.team{top:3314px;height:340px}
.member{position:absolute;top:7px;width:230px;text-align:center}
.member .photo{position:relative;height:222px}
.member p{font-size:9px;line-height:1.5;margin-top:14px;padding:0 8px}
.social{display:flex;justify-content:center;gap:12px;margin-top:14px}
.social span{width:8px;height:8px;border-radius:50%;background:var(--accent)}

/* partners */
.partners{top:3689px;height:443px;display:grid;grid-template-columns:repeat(4,300px);grid-template-rows:repeat(2,221.5px)}
.partner{display:flex;align-items:center;justify-content:center;font-weight:700;color:var(--white);font-size:16px;letter-spacing:.04em}

/* news */
.news{top:4160px;height:490px}
.news h2{left:240px;top:18px;font-size:24px;font-weight:700;line-height:1.1;color:var(--ink)}
.news .bar{left:240px;top:84px}
.news .intro{left:428px;top:18px;width:530px}
.post{position:absolute;top:125px;width:226px;height:340px;background:var(--white);box-shadow:0 2px 8px rgba(0,0,0,.09)}
.post .photo{position:relative;height:125px}
.post .body{padding:12px 16px}
.post .cat{font-size:8px;color:var(--accent);font-weight:600}
.post h4{font-size:14px;font-weight:700;color:var(--ink);line-height:1.2;margin:2px 0 10px}
.post p{font-size:9px;line-height:1.5}
.post .meta{display:flex;justify-content:space-between;font-size:8px;margin-top:16px;color:var(--muted)}
.post .meta b{color:var(--ink)}

/* newsletter */
.newsletter{top:4671px;height:186px;background:var(--accent-soft)}
.newsletter h3{left:0;width:1200px;top:56px;text-align:center;font-size:13px;font-weight:700;color:var(--white)}
.newsletter .field{left:418px;top:100px;width:235px;height:29px;background:var(--white);font-size:9px;color:var(--muted);padding:7px 14px}
.newsletter .btn{left:653px;top:100px;width:115px;height:29px;padding-top:9px}

/* instagram */
.insta{top:4892px;height:190px}
.insta h3{left:240px;top:60px;font-size:14px;font-weight:700;color:var(--ink)}
.insta .handle{left:240px;top:82px;font-size:8px;color:var(--accent)}
.insta .photo{top:8px;height:164px}

/* footer */
.footer{top:5142px;height:215px;background:var(--soft)}
.fcol{position:absolute;top:26px;font-size:8.5px;line-height:1.7}
.fcol h4{font-size:11px;font-weight:700;color:var(--ink);margin-bottom:8px;display:flex;align-items:center;gap:5px}
.fcol .field{width:150px;border-bottom:1px solid var(--line);padding:2px 0;color:var(--muted)}
.fcol .sub{margin-top:8px;color:var(--accent);font-weight:600}
.footer .social{position:absolute;left:830px;top:140px;gap:10px}
.footer .copy{left:240px;top:185px;font-size:8px;color:var(--muted)}
</style>
</head>
<body>

<header class="nav">
  <span class="brand">fern+lantern</span>
  <a>home ▾</a><a>about us ▾</a><a>services ▾</a><a>news ▾</a><a>pages ▾</a><a>shop ▾</a>
  <div class="phones">
    <span><svg width="9" height="9" viewBox="0 0 10 10" fill="none" stroke="#33b8a4" stroke-width="1.2"><path d="M2 1h2l1 2.5-1.2.8a5 5 0 0 0 2 2l.8-1.2L9 6v2a1 1 0 0 1-1 1A7 7 0 0 1 1 2a1 1 0 0 1 1-1z"/></svg>555 0142</span>
    <span><svg width="9" height="9" viewBox="0 0 10 10" fill="none" stroke="#33b8a4" stroke-width="1.2"><path d="M2 1h2l1 2.5-1.2.8a5 5 0 0 0 2 2l.8-1.2L9 6v2a1 1 0 0 1-1 1A7 7 0 0 1 1 2a1 1 0 0 1 1-1z"/></svg>555 0187</span>
  </div>
</header>

<section class="hero">
  <div class="photo" role="img" aria-label="Photo of a bearded patient in a denim shirt wearing glasses"></div>
  <h1 class="abs">make an appointment.</h1>
  <p class="abs">Book an eye exam at either of our clinics and meet our friendly team of vision care experts.</p>
  <span class="abs btn btn-white b1">contact us</span>
  <span class="abs btn btn-accent b2">schedule visit</span>
</section>

<section class="what">
  <h2 class="abs">what we do<br>the best!</h2>
  <div class="abs bar"></div>
  <p class="abs intro">Lorem ipsum dolor sit amet, consectetur adipiscing elit, sed diam nonummy nibh euismod tincidunt ut laoreet dolore magna aliquam erat volutpat. Ut wisi enim ad minim veniam, quis nostrud exerci tation ullamcorper suscipit lobortis nisl ut aliquip ex ea commodo consequat. Duis autem vel eum iriure dolor in hendrerit in vulputate velit esse molestie consequat.</p>

  <div class="feature" style="left:240px;top:138px"><svg width="18" height="18" viewBox="0 0 18 18" fill="none" stroke="#33b8a4" stroke-width="1.3"><circle cx="9" cy="9" r="7"/><circle cx="9" cy="9" r="2.5"/></svg><h4>contact lenses</h4><p>Ut wisi enim ad minim veniam, quis nostrud exerci tation ullamcorper suscipit lobortis nisl ut aliquip.</p></div>
  <div class="feature" style="left:482px;top:138px"><svg width="18" height="18" viewBox="0 0 18 18" fill="none" stroke="#33b8a4" stroke-width="1.3"><rect x="2" y="3" width="14" height="10" rx="1"/><path d="M6 16h6"/></svg><h4>vision care</h4><p>Lorem ipsum dolor sit amet, consectetur adipiscing elit, sed diam nonummy nibh euismod.</p></div>
  <div class="feature" style="left:768px;top:138px"><svg width="18" height="18" viewBox="0 0 18 18" fill="none" stroke="#33b8a4" stroke-width="1.3"><path d="M1 9s3-5 8-5 8 5 8 5-3 5-8 5-8-5-8-5z"/><circle cx="9" cy="9" r="2"/></svg><h4>eye exams</h4><p>Duis autem vel eum iriure dolor in hendrerit in vulputate velit esse molestie consequat.</p></div>
  <div class="feature" style="left:240px;top:234px"><svg width="18" height="18" viewBox="0 0 18 18" fill="none" stroke="#33b8a4" stroke-width="1.3"><circle cx="9" cy="9" r="7"/><path d="M5 9l3 3 5-6"/></svg><h4>vision correction</h4><p>Ut wisi enim ad minim veniam, quis nostrud exerci tation ullamcorper suscipit lobortis nisl ut aliquip.</p></div>
  <div class="feature" style="left:482px;top:234px"><svg width="18" height="18" viewBox="0 0 18 18" fill="none" stroke="#33b8a4" stroke-width="1.3"><rect x="3" y="2" width="12" height="14" rx="1"/><path d="M9 6v6M6 9h6"/></svg><h4>eye diseases</h4><p>Lorem ipsum dolor sit amet, consectetur adipiscing elit, sed diam nonummy nibh euismod.</p></div>
  <div class="feature" style="left:768px;top:234px"><svg width="18" height="18" viewBox="0 0 18 18" fill="none" stroke="#33b8a4" stroke-width="1.3"><circle cx="5" cy="10" r="3.5"/><circle cx="13" cy="10" r="3.5"/><path d="M8.5 10h1"/></svg><h4>glasses and frames</h4><p>Duis autem vel eum iriure dolor in hendrerit in vulputate velit esse molestie consequat.</p></div>
</section>

<section class="unique">
  <h2 class="abs">unique services</h2>
  <div class="abs bar"></div>
  <p class="abs">Lorem ipsum dolor sit amet, consectetur adipiscing elit, sed diam nonummy nibh euismod tincidunt ut laoreet dolore magna aliquam erat volutpat wisi enim.</p>
  <span class="abs btn btn-outline-white">view more</span>
</section>

<section class="pricing">
  <h2 class="abs">we offer the best</h2>
  <div class="abs bar"></div>
  <div class="plan" style="left:240px;width:224px">
    <svg width="22" height="22" viewBox="0 0 22 22" fill="none" stroke="#33b8a4" stroke-width="1.4"><rect x="3" y="4" width="16" height="15" rx="1"/><path d="M3 9h16M7 2v4M15 2v4M7 13h2M11 13h2M15 13h1M7 16h2M11 16h2"/></svg>
    <h4>basic</h4><div class="per">plan</div>
    <div class="price">49$</div><div class="per">per month</div>
    <ul><li>Yearly eye exam included</li><li>Basic lens cleaning</li><li>Frame adjustment visits</li><li>Online appointment booking</li></ul>
    <span class="btn btn-outline-accent">view more</span>
  </div>
  <div class="plan" style="left:475px;width:232px">
    <svg width="22" height="22" viewBox="0 0 22 22" fill="none" stroke="#33b8a4" stroke-width="1.4"><rect x="3" y="2" width="16" height="18" rx="1"/><path d="M7 7h8M7 11h8M7 15h5"/></svg>
    <h4>standard</h4><div class="per">plan</div>
    <div class="price">99$</div><div class="per">per month</div>
    <ul><li>Two eye exams per year</li><li>Contact lens fitting</li><li>Frame adjustment visits</li><li>Priority appointment booking</li></ul>
    <span class="btn btn-outline-accent">view more</span>
  </div>
  <div class="plan" style="left:725px;width:232px">
    <svg width="22" height="22" viewBox="0 0 22 22" fill="none" stroke="#33b8a4" stroke-width="1.4"><rect x="2" y="5" width="18" height="13" rx="1"/><path d="M2 6l9 7 9-7"/></svg>
    <h4>professional</h4><div class="per">plan</div>
    <div class="price">199$</div><div class="per">per month</div>
    <ul><li>Unlimited eye exams</li><li>Contact lens supply</li><li>Eye disease screening</li><li>Dedicated care coordinator</li></ul>
    <span class="btn btn-outline-accent">view more</span>
  </div>
</section>

<section class="about">
  <h2 class="abs">about us</h2>
  <div class="abs bar"></div>
  <p class="abs">Lorem ipsum dolor sit amet, consectetur adipiscing elit, sed diam nonummy nibh euismod tincidunt ut laoreet dolore magna aliquam erat volutpat. Ut wisi enim ad minim veniam, quis nostrud exerci tation ullamcorper suscipit lobortis nisl ut aliquip ex ea commodo.</p>
  <span class="abs btn btn-white">read more</span>
</section>

<section class="services">
  <div class="svc" style="left:242px;top:0"><div class="circ"><svg width="16" height="16" viewBox="0 0 16 16" fill="none" stroke="#33b8a4" stroke-width="1.2"><path d="M2 8l6-5 6 5v6H2z"/></svg></div><h4>contact lenses</h4><p>Lorem ipsum dolor sit amet, consectetur adipiscing elit, sed diam nonummy nibh euismod tincidunt ut laoreet dolore magna.</p></div>
  <div class="svc" style="left:485px;top:0"><div class="circ"><svg width="16" height="16" viewBox="0 0 16 16" fill="none" stroke="#33b8a4" stroke-width="1.2"><rect x="2" y="3" width="12" height="9"/></svg></div><h4>vision care</h4><p>Lorem ipsum dolor sit amet, consectetur adipiscing elit, sed diam nonummy nibh euismod tincidunt ut laoreet dolore magna.</p></div>
  <div class="svc" style="left:728px;top:0"><div class="circ"><svg width="16" height="16" viewBox="0 0 16 16" fill="none" stroke="#33b8a4" stroke-width="1.2"><path d="M1 8s3-4 7-4 7 4 7 4-3 4-7 4-7-4-7-4z"/><circle cx="8" cy="8" r="1.6"/></svg></div><h4>eye exams</h4><p>Lorem ipsum dolor sit amet, consectetur adipiscing elit, sed diam nonummy nibh euismod tincidunt ut laoreet dolore magna.</p></div>
  <div class="svc" style="left:242px;top:186px"><div class="circ"><svg width="16" height="16" viewBox="0 0 16 16" fill="none" stroke="#33b8a4" stroke-width="1.2"><circle cx="8" cy="8" r="6"/><path d="M5 8l2 2 4-4"/></svg></div><h4>vision correction</h4><p>Lorem ipsum dolor sit amet, consectetur adipiscing elit, sed diam nonummy nibh euismod tincidunt ut laoreet dolore magna.</p></div>
  <div class="svc" style="left:485px;top:186px"><div class="circ"><svg width="16" height="16" viewBox="0 0 16 16" fill="none" stroke="#33b8a4" stroke-width="1.2"><rect x="3" y="2" width="10" height="12"/><path d="M8 5v6M5 8h6"/></svg></div><h4>eye diseases</h4><p>Lorem ipsum dolor sit amet, consectetur adipiscing elit, sed diam nonummy nibh euismod tincidunt ut laoreet dolore magna.</p></div>
  <div class="svc" style="left:728px;top:186px"><div class="circ"><svg width="16" height="16" viewBox="0 0 16 16" fill="none" stroke="#33b8a4" stroke-width="1.2"><circle cx="7" cy="7" r="4.5"/><path d="M10.5 10.5L14 14"/></svg></div><h4>glasses and frames</h4><p>Lorem ipsum dolor sit amet, consectetur adipiscing elit, sed diam nonummy nibh euismod tincidunt ut laoreet dolore magna.</p></div>
</section>

<section class="split" style="top:2053px">
  <div class="textside" style="left:0">
    <h3>eye exams</h3>
    <p>Sed diam nonummy nibh euismod tincidunt ut laoreet dolore magna aliquam erat volutpat ut wisi enim ad minim veniam quis.</p>
    <span class="link">see details</span>
  </div>
  <div class="photo" style="left:600px;top:0;width:600px;height:447px;background:radial-gradient(ellipse at 40% 40%,#6a6b70 0%,#3c3d41 55%,#232326 100%)" role="img" aria-label="Photo of dark framed eyeglasses resting on a grey surface"></div>
</section>

<section class="split" style="top:2500px">
  <div class="photo" style="left:0;top:0;width:600px;height:447px;background:linear-gradient(135deg,#3d5b34 0%,#8f3a2c 45%,#c8523d 70%,#d9cbb7 100%)" role="img" aria-label="Photo of a person in a plaid shirt holding sunglasses outdoors"></div>
  <div class="textside" style="left:600px;background:var(--white)">
    <h3>vision correction</h3>
    <p>Sed diam nonummy nibh euismod tincidunt ut laoreet dolore magna aliquam erat volutpat ut wisi enim ad minim veniam quis.</p>
    <span class="link">see details</span>
  </div>
</section>

<section class="testi">
  <span class="abs arrow" style="left:243px">‹</span>
  <div class="abs avatar" role="img" aria-label="Portrait photo of a patient"></div>
  <h4 class="abs">marla venn</h4>
  <div class="abs role">Patient</div>
  <p class="abs">Lorem ipsum dolor sit amet, consectetur adipiscing elit, sed diam nonummy nibh euismod tincidunt ut laoreet dolore magna aliquam erat volutpat. Ut wisi enim ad minim veniam, quis nostrud exerci tation ullamcorper suscipit lobortis nisl.</p>
  <span class="abs arrow" style="left:946px">›</span>
</section>

<section class="team">
  <div class="member" style="left:240px">
    <div class="photo" style="background:linear-gradient(160deg,#d9d9d9,#a24a4a 70%,#6d2f2f)" role="img" aria-label="Team member portrait, man in glasses and red shirt"></div>
    <p>Lorem ipsum dolor sit amet, consectetur adipiscing elit, sed diam nonummy nibh euismod tincidunt ut laoreet dolore magna.</p>
    <div class="social"><span></span><span></span><span></span><span></span><span></span></div>
  </div>
  <div class="member" style="left:484px">
    <div class="photo" style="background:linear-gradient(160deg,#e0e0e0,#6b6b6b 65%,#2d2d2d)" role="img" aria-label="Team member portrait, bearded man in a dark t-shirt"></div>
    <p>Lorem ipsum dolor sit amet, consectetur adipiscing elit, sed diam nonummy nibh euismod tincidunt ut laoreet dolore magna.</p>
    <div class="social"><span></span><span></span><span></span><span></span><span></span></div>
  </div>
  <div class="member" style="left:727px">
    <div class="photo" style="background:linear-gradient(160deg,#e6e4e1,#b9a89a 60%,#7d6c60)" role="img" aria-label="Team member portrait, woman in a grey top"></div>
    <p>Lorem ipsum dolor sit amet, consectetur adipiscing elit, sed diam nonummy nibh euismod tincidunt ut laoreet dolore magna.</p>
    <div class="social"><span></span><span></span><span></span><span></span><span></span></div>
  </div>
</section>

<section class="partners">
  <div class="partner" style="background:var(--dark1)">brightmoor</div>
  <div class="partner" style="background:var(--dark3)">tallowby</div>
  <div class="partner" style="background:var(--dark2)">quillby</div>
  <div class="partner" style="background:var(--dark1)">harborline</div>
  <div class="partner" style="background:var(--dark3)">cedar row</div>
  <div class="partner" style="background:var(--dark2)">ostrava</div>
  <div class="partner" style="background:var(--dark1)">lumenfield</div>
  <div class="partner" style="background:var(--dark3)">thornwick</div>
</section>

<section class="news">
  <h2 class="abs">our latest<br>news</h2>
  <div class="abs bar"></div>
  <p class="abs intro">Lorem ipsum dolor sit amet, consectetur adipiscing elit, sed diam nonummy nibh euismod tincidunt ut laoreet dolore magna aliquam erat volutpat. Ut wisi enim ad minim veniam, quis nostrud exerci tation ullamcorper suscipit lobortis nisl ut aliquip ex ea commodo consequat.</p>

  <article class="post" style="left:240px">
    <div class="photo" style="background:linear-gradient(135deg,#eeeeee,#b8bcc0)" role="img" aria-label="Photo of a person working at a whiteboard"></div>
    <div class="body"><div class="cat">vision tips</div><h4>how to avoid computer eye strain?</h4><p>Lorem ipsum dolor sit amet, consectetur adipiscing elit, sed diam nonummy nibh euismod tincidunt ut laoreet dolore.</p><div class="meta"><span>March 10, 2024</span><b>read more →</b></div></div>
  </article>
  <article class="post" style="left:484px">
    <div class="photo" style="background:linear-gradient(135deg,#d4d4d4,#4a4a4a)" role="img" aria-label="Black and white photo of a woman smoking"></div>
    <div class="body"><div class="cat">health</div><h4>wait, smoking is very bad for your eyes?</h4><p>Lorem ipsum dolor sit amet, consectetur adipiscing elit, sed diam nonummy nibh euismod tincidunt ut laoreet dolore.</p><div class="meta"><span>March 12, 2024</span><b>read more →</b></div></div>
  </article>
  <article class="post" style="left:731px">
    <div class="photo" style="background:linear-gradient(180deg,#b6cfd6,#8fa88a 60%,#c7b79c)" role="img" aria-label="Photo of people walking along a coastal path"></div>
    <div class="body"><div class="cat">lifestyle</div><h4>do more sport, get a better vision!</h4><p>Lorem ipsum dolor sit amet, consectetur adipiscing elit, sed diam nonummy nibh euismod tincidunt ut laoreet dolore.</p><div class="meta"><span>March 15, 2024</span><b>read more →</b></div></div>
  </article>
</section>

<section class="newsletter">
  <h3 class="abs">sign up for our newsletter</h3>
  <div class="abs field">Enter your email</div>
  <span class="abs btn btn-accent">subscribe</span>
</section>

<section class="insta">
  <h3 class="abs">instagram</h3>
  <div class="abs handle">@fernlantern_clinic</div>
  <div class="photo" style="left:428px;width:143px;background:linear-gradient(135deg,#d9b8a0,#8a5c48)" role="img" aria-label="Photo of a couple embracing"></div>
  <div class="photo" style="left:607px;width:143px;background:linear-gradient(135deg,#3bb7d8,#f0a6a0)" role="img" aria-label="Photo of sunglasses on a bright background"></div>
  <div class="photo" style="left:786px;width:150px;background:linear-gradient(135deg,#d8d0c4,#3a332e)" role="img" aria-label="Photo of a woman in a dark coat"></div>
</section>

<footer class="footer">
  <div class="fcol" style="left:240px"><h4><svg width="8" height="10" viewBox="0 0 8 10" fill="none" stroke="#33b8a4" stroke-width="1.2"><path d="M4 9.5S1 6 1 4a3 3 0 0 1 6 0c0 2-3 5.5-3 5.5z"/><circle cx="4" cy="4" r="1"/></svg>ashcombe</h4>14 Alder Street<br>North Quarter<br>Ashcombe<br>Tel: 555 0142</div>
  <div class="fcol" style="left:428px"><h4><svg width="8" height="10" viewBox="0 0 8 10" fill="none" stroke="#33b8a4" stroke-width="1.2"><path d="M4 9.5S1 6 1 4a3 3 0 0 1 6 0c0 2-3 5.5-3 5.5z"/><circle cx="4" cy="4" r="1"/></svg>harlow point</h4>220 Birch Avenue<br>Harbor District<br>Harlow Point<br>Tel: 555 0187</div>
  <div class="fcol" style="left:607px"><h4><svg width="8" height="10" viewBox="0 0 8 10" fill="none" stroke="#33b8a4" stroke-width="1.2"><path d="M4 9.5S1 6 1 4a3 3 0 0 1 6 0c0 2-3 5.5-3 5.5z"/><circle cx="4" cy="4" r="1"/></svg>westbrae</h4>9 Linden Road<br>Old Town<br>Westbrae<br>Tel: 555 0163</div>
  <div class="fcol" style="left:793px"><h4>newsletter</h4><div class="field">Your Email Address</div><div class="sub">subscribe now</div></div>
  <div class="social"><span></span><span></span><span></span><span></span><span></span></div>
  <div class="abs copy">© 2024 fern+lantern, complete vision care. All rights reserved.</div>
</footer>

</body>
</html>
```